Electronic Music Artist needs an Album Cover

DRELL is an electronic musician from Boston, Massachusetts. He needs an album cover that captures the essence of his music. The album is called Lanterns, which represents his experiences growing up, positive and negative. He would like to see designs that involves color and creativity. Attached are some examples of artworks that DRELL likes. He also included a few of his original photos (optional to use. Using a photo will not effect his final decision!), and his logo.

Colors

Designer to choose colors to be used in the design.

Requirements
Must have
• My project must have the text "Lanterns" and "DRELL", and the logo (attached in the files). The logo should not be the main subject of the artwork. Everything must look aesthetically pleasing.
Nice to have
• It would be nice to have some sort of creative graphic design (see example album covers for reference). Also, in one of the references, there is a column on the left hand side with some text in it. That could be cool to include, but without the asian text.
Should not have
• The project should not have any other language besides English.

```html
<!DOCTYPE html>
<html lang="en">
<head>
<meta charset="UTF-8">
<title>DRELL — Lanterns</title>
<link rel="stylesheet" href="https://fonts.googleapis.com/css2?family=Archivo:wght@700&display=swap">
<style>
  :root {
    --deep-green: #0a2612;
    --forest-green: #0f4a1c;
    --glow-teal: rgba(120, 200, 185, 0.55);
    --glow-white: rgba(215, 235, 230, 0.6);
    --artist-grey: #d6dedb;
    --title-grey: #8a9893;
    --mark-teal: #8fd6c6;
  }
  html, body {
    margin: 0;
    padding: 0;
    width: 1174px;
    height: 1200px;
    overflow: hidden;
    background: var(--deep-green);
  }
  .album-cover {
    position: relative;
    width: 1174px;
    height: 1200px;
    overflow: hidden;
    font-family: "Archivo", Arial, sans-serif;
  }
  .light-streak {
    position: absolute;
    inset: 0;
    background:
      radial-gradient(ellipse 300px 70px at 560px 590px, var(--glow-white), transparent 70%),
      radial-gradient(ellipse 640px 120px at 640px 580px, var(--glow-teal), transparent 72%),
      radial-gradient(ellipse 520px 90px at 1020px 520px, rgba(120, 200, 185, 0.4), transparent 70%),
      radial-gradient(ellipse 420px 160px at 180px 700px, rgba(90, 170, 150, 0.35), transparent 70%),
      radial-gradient(ellipse 420px 380px at 80px 120px, rgba(20, 110, 35, 0.7), transparent 75%),
      radial-gradient(ellipse 700px 500px at 600px 300px, rgba(20, 80, 40, 0.6), transparent 75%),
      linear-gradient(180deg, var(--forest-green) 0%, #0b3217 50%, var(--deep-green) 100%);
  }
  .cover-title {
    position: absolute;
    left: 0;
    width: 100%;
    top: 390px;
    margin: 0;
    text-align: center;
    font-size: 40px;
    font-weight: 700;
    letter-spacing: 0.5px;
    line-height: 1;
  }
  .cover-title .artist { color: var(--artist-grey); }
  .cover-title .album { color: var(--title-grey); text-transform: uppercase; }
  .artist-mark {
    position: absolute;
    left: 430px;
    top: 435px;
    width: 312px;
    height: 330px;
    display: flex;
    align-items: center;
    justify-content: center;
    color: var(--mark-teal);
    font-size: 86px;
    font-weight: 700;
    opacity: 0.85;
  }
</style>
</head>
<body>
  <main class="album-cover">
    <div class="light-streak" role="img" aria-label="Abstract horizontal burst of teal and white light across a dark green haze"></div>
    <h1 class="cover-title"><span class="artist">DRELL</span> <span class="album">Lanterns</span></h1>
    <div class="artist-mark">DRELL</div>
  </main>
</body>
</html>
```